Wordpress Design Project for Bankruptcy Law Office in San Francisco

our current website: www.dorvanetzlaw.example

we would like to re-design it for wordpress to make it faster and a bit more modern.

content should be similar to what we have there right now but also we do family law

please include logo for law office:

Law Office of Marta K. Zelobrodna

Thank you.
Updates

please see attached word document with logos that we like as an example.

we do tend to like color red.  darker red.

Please submit your design variations and logo as soon as possible.   We would like to go over them and make our decision

Reason: Please create couple of more variations of logo for your design, so we can make our decision what we like the most. Please see word doc for samples: Text: Law Office Of Marta K. Zelobrodna

Reason: final touches

Target Market(s)

bankruptcy and family law clients

Industry/Entity Type

Family Law

Requirements
Must have
• see examples of law sites
http://outreach.lexorvin.example/testimonials

- new logo: Law Office of Marta K. Zelobrodna
- client intake form
- blog
- contact us form

Nice to have
• - map
- red color
- on the front page a nice photo of SF or a happy family

```html
<!DOCTYPE html>
<html lang="en">
<head>
<meta charset="utf-8">
<title>Varnholt Law Office</title>
<link rel="stylesheet" href="https://fonts.googleapis.com/css2?family=Arimo:wght@400;700&family=Cinzel:wght@400;700&family=Yanone+Kaffeesatz:wght@400;600&display=swap">
<style>
:root{
  --teal:#1f6b5d;
  --teal-dark:#0f3e37;
  --gold:#f6b43a;
  --cream:#f7d79a;
  --cream-light:#fdf3df;
  --text:#6b6b6b;
  --ink:#3a3a3a;
  --red:#a83c3c;
  --panel:#e2e2e2;
}
*{margin:0;padding:0;box-sizing:border-box}
html,body{width:947px;height:1200px;overflow:hidden;background:#fff;font-family:Arimo,Arial,sans-serif}
.page{position:relative;width:947px;height:1200px}
.site-header{position:absolute;left:0;top:0;width:947px;height:108px;background:linear-gradient(90deg,var(--cream-light) 0%,#fbe6bd 40%,var(--cream) 100%)}
.brand{position:absolute;left:60px;top:54px;width:222px;text-align:center;font-family:Arimo,Arial,sans-serif;font-weight:400;font-size:20px;color:var(--ink)}
.social{position:absolute;right:37px;top:47px;display:flex;gap:5px}
.social span{width:22px;height:22px;background:var(--ink);border-radius:3px}
.call{position:absolute;right:37px;top:82px;font-size:17px;color:#111}
.main-nav{position:absolute;left:0;top:108px;width:947px;height:42px;background:linear-gradient(#2c7d6e,var(--teal) 55%,#185a4e);display:flex}
.main-nav a{color:#fff;text-decoration:none;font-size:17px;line-height:42px;text-align:center;border-right:1px solid #14493f;white-space:nowrap}
.main-nav a:last-child{border-right:0}
.slider{position:absolute;left:62px;top:170px;width:833px;height:313px;background:var(--gold);padding:10px}
.slide{position:relative;width:100%;height:100%;background:linear-gradient(90deg,#3b2a1f,#6b4a32 30%,#2a1d15 70%,#3a2a20)}
.slide-text{position:absolute;right:26px;top:38px;text-align:right;color:#fff;font-family:"Yanone Kaffeesatz",sans-serif;font-size:41px;line-height:40px}
.slide-text b{font-size:62px;line-height:62px;font-weight:600}
.arrow{position:absolute;top:303px;width:42px;height:42px;border-radius:50%;background:#9c9c80}
.arrow svg{position:absolute;top:12px}
.arrow.prev{left:43px}.arrow.next{left:872px}
.feature{position:absolute;top:502px;width:278px}
.feature h2,.info h2{font-family:Cinzel,serif;font-weight:400;color:var(--teal);letter-spacing:.3px;white-space:nowrap}
.feature h2{font-size:16px}
.feature .photo{margin-top:16px;height:104px;border:3px solid var(--teal)}
.feature p{margin-top:19px;font-size:11px;line-height:18px;color:var(--text);text-align:justify;padding:0 2px}
.btn{position:absolute;display:flex;height:30px;border-radius:3px;overflow:hidden;font-weight:700;font-size:13px;color:#fff;box-shadow:0 1px 2px rgba(0,0,0,.3)}
.btn .label{background:linear-gradient(#2f8272,#175a4d);padding:0 10px;line-height:30px}
.btn .go{background:linear-gradient(#f9c64e,#e9a01f);width:25px;line-height:30px;text-align:center;font-size:12px}
.feature .btn{right:0;top:225px}
.rule{position:absolute;top:775px;height:1px;background:#ddd}
.info{position:absolute;left:62px;top:808px;width:552px}
.info h2{font-size:25px}
.info p{margin-top:17px;font-size:13px;line-height:23px;color:var(--text);text-align:justify}
.info p+p{margin-top:23px}
.info .btn{right:0;top:263px}
.contact{position:absolute;left:630px;top:793px;width:267px;height:307px;background:var(--panel);border-radius:14px;border:3px solid #f0f0f0}
.contact h3{position:absolute;left:34px;top:0;width:203px;height:43px;background:linear-gradient(#e8dc8c,#bfae4a);font-family:Cinzel,serif;font-weight:400;color:#fff;font-size:16px;letter-spacing:1px;text-align:center;line-height:43px}
.field{position:absolute;left:15px;width:234px;height:18px;background:var(--red);color:#fff;font-family:Georgia,serif;font-size:10px;padding:2px 8px}
.field.msg{height:68px}
.submit{position:absolute;left:100px;top:272px;width:68px;height:20px;background:linear-gradient(#fbd5d0,#e7a8a2);font-size:8px;font-weight:700;letter-spacing:1px;color:#7a3b36;text-align:center;line-height:20px;border-radius:2px}
.site-footer{position:absolute;left:0;top:1142px;width:947px;height:58px;background:var(--teal-dark);color:#fff;font-size:12px;padding:22px 0 0 64px}
</style>
</head>
<body>
<div class="page">
  <header class="site-header">
    <div class="brand">Varnholt Law Office</div>
    <div class="social"><span></span><span></span><span></span></div>
    <div class="call">Call Us Now : 000–000–000</div>
  </header>
  <nav class="main-nav">
    <a href="#" style="width:138px">Home</a><a href="#" style="width:124px">About Us</a><a href="#" style="width:192px">Areas of Practice</a><a href="#" style="width:141px">Resources</a><a href="#" style="width:97px">Blog</a><a href="#" style="width:90px">Faq</a><a href="#" style="width:165px">Contact Us</a>
  </nav>

  <section class="slider">
    <div class="slide" role="img" aria-label="Hand resting on a bible for an oath">
      <div class="slide-text">We offer<br>our clients<br>an expert<br><b>LEGAL</b><br>advice.</div>
    </div>
  </section>
  <div class="arrow prev"><svg width="42" height="18" viewBox="0 0 42 18"><path d="M17 2 10 9l7 7" fill="none" stroke="#fff" stroke-width="3"/></svg></div>
  <div class="arrow next"><svg width="42" height="18" viewBox="0 0 42 18"><path d="M25 2l7 7-7 7" fill="none" stroke="#fff" stroke-width="3"/></svg></div>

  <article class="feature" style="left:62px">
    <h2>More Than Just a Lawyer</h2>
    <div class="photo" role="img" aria-label="Team of lawyers standing outside a courthouse" style="background:linear-gradient(90deg,#6f6a64,#b9b3ab,#4d4a48)"></div>
    <p>Lorem ipsum dolor sit amet, consectetuer adipiscing elit, sed diam nonummy nibh euismod tincidunt ut laoreet dolore magna aliquam erat volutpat.</p>
    <a class="btn"><span class="label">Read More</span><span class="go">GO</span></a>
  </article>
  <article class="feature" style="left:346px">
    <h2>Free Attorney Consultation</h2>
    <div class="photo" role="img" aria-label="Judge's wig beside law books" style="background:linear-gradient(90deg,#5a3a22,#d9b27a 45%,#1d4a2c)"></div>
    <p>Lorem ipsum dolor sit amet, consectetuer adipiscing elit, sed diam nonummy nibh euismod tincidunt ut laoreet dolore magna aliquam erat volutpat.</p>
    <a class="btn"><span class="label">Read More</span><span class="go">GO</span></a>
  </article>
  <article class="feature" style="left:629px">
    <h2>Understand the Alternatives</h2>
    <div class="photo" role="img" aria-label="Two businessmen reviewing a document" style="background:linear-gradient(90deg,#eef0ef,#6c6c70 45%,#e6eae8)"></div>
    <p>Lorem ipsum dolor sit amet, consectetuer adipiscing elit, sed diam nonummy nibh euismod tincidunt ut laoreet dolore magna aliquam erat volutpat.</p>
    <a class="btn"><span class="label">Read More</span><span class="go">GO</span></a>
  </article>

  <div class="rule" style="left:62px;width:552px"></div>
  <div class="rule" style="left:629px;width:267px"></div>

  <section class="info">
    <h2>Important Information</h2>
    <p>The Law Offices of Marta K. Zelobrodna is a consumer law office dedicated to consumer protection and zealously defending the rights of our clients.&nbsp; We offer the big firm quality legal representation with a small firm individualized attention to each client.</p>
    <p>Our office offers services in: all types of consumer bankruptcy filings, i.e. Chapter 7, Chapter 13, Chapter 11, negotiating a settlement of your debts, assisting you in the defense of collection litigation and defending you against foreclosure. Please review our site and see what we may be able to offer you. Feel free to call us at (415) 555-0148 or use our free case evaluation form.</p>
    <a class="btn"><span class="label">Read More</span><span class="go">GO</span></a>
  </section>

  <aside class="contact">
    <h3>CONTACT FORM</h3>
    <div class="field" style="top:78px">Name:</div>
    <div class="field" style="top:106px">E-mail:</div>
    <div class="field" style="top:132px">Phone:</div>
    <div class="field" style="top:159px">Subject:</div>
    <div class="field msg" style="top:183px">Message:</div>
    <div class="submit">SUBMIT</div>
  </aside>

  <footer class="site-footer">copyright@2012.All rights reserved.</footer>
</div>
</body>
</html>
```